Floristry Business Card Design Project

I have a logo now and am looking to incorporate this into a business card. I would like a double sided business card. I would like one side to be decorative so that it blends well when included with floral arrangements and that can also be used as the front of a card and the other side will contain the business details. The font on the business details side should be clear although some decorative font would be ok. I have included the logo files for use in the business card design.

Feel free to break up the logo and use certain aspects of it in the design. Really looking for something that stands out and that is really creative.

Industry/Entity Type

Floral

Requirements
Should not have
• Nothing tacky or corny. The logo should be clearly read (perhaps a background colour).

```html
<!DOCTYPE html>
<html lang="en">
<head>
<meta charset="utf-8">
<title>Meadow Lane – Business Card</title>
<link rel="stylesheet" href="https://fonts.googleapis.com/css2?family=Great+Vibes&family=Cormorant+Garamond:wght@500&family=Raleway:wght@400&display=swap">
<style>
  :root {
    --page: #e7e4df;
    --card: #ffffff;
    --mint: #8fc9ab;
    --mint-soft: #cfe7da;
    --leaf: #b9d27a;
    --leaf-soft: #e6efcc;
    --blush: #f1b3a4;
    --ink-soft: #7fbf9f;
  }
  * { margin: 0; padding: 0; box-sizing: border-box; }
  html, body { width: 1200px; height: 855px; overflow: hidden; }
  body {
    background: var(--page);
    display: flex;
    align-items: center;
    justify-content: center;
    gap: 60px;
    font-family: "Raleway", sans-serif;
  }
  .card {
    position: relative;
    width: 520px;
    height: 300px;
    background: var(--card);
    border-radius: 22px;
    overflow: hidden;
    box-shadow: 0 2px 10px rgba(0,0,0,0.08);
  }

  /* Decorative side */
  .pattern {
    position: absolute;
    border-radius: 50%;
    filter: blur(2px);
  }
  .pattern--top {
    top: -90px; right: -60px; width: 380px; height: 200px;
    background: radial-gradient(ellipse at center, var(--mint-soft) 0%, var(--leaf-soft) 55%, rgba(255,255,255,0) 75%);
  }
  .pattern--bottom {
    bottom: -100px; left: -70px; width: 420px; height: 220px;
    background: radial-gradient(ellipse at center, var(--mint-soft) 0%, var(--leaf-soft) 55%, rgba(255,255,255,0) 75%);
  }
  .front-brand {
    position: absolute;
    inset: 0;
    display: flex;
    align-items: center;
    justify-content: center;
    gap: 14px;
  }
  .brand-dot {
    width: 22px; height: 22px;
    border: 1.5px solid var(--mint);
    border-radius: 50%;
  }
  .front-brand__name {
    font-family: "Cormorant Garamond", serif;
    font-weight: 500;
    font-size: 20px;
    letter-spacing: 6px;
    text-transform: uppercase;
    color: var(--mint);
  }

  /* Details side */
  .wreath {
    position: absolute;
    top: -70px; left: 50px;
    width: 190px; height: 170px;
    border-radius: 50%;
    background: radial-gradient(circle at center, #ffffff 0%, #ffffff 48%, var(--mint-soft) 60%, var(--leaf-soft) 70%, #fbe1da 78%, rgba(255,255,255,0) 86%);
  }
  .back-title {
    position: absolute;
    top: 62px; right: 30px;
    font-family: "Great Vibes", cursive;
    font-size: 54px;
    color: var(--mint);
    line-height: 1;
  }
  .contact {
    position: absolute;
    left: 30px; top: 125px;
    width: 200px;
  }
  .contact__name {
    font-family: "Great Vibes", cursive;
    font-size: 26px;
    color: var(--mint);
    line-height: 1;
  }
  .contact__role {
    font-size: 12px;
    color: var(--leaf);
    margin: 4px 0 10px;
    text-align: right;
    padding-right: 30px;
  }
  .contact__line {
    display: flex;
    align-items: center;
    gap: 6px;
    font-size: 12.5px;
    color: var(--leaf);
    margin-bottom: 5px;
  }
  .contact__line svg { width: 13px; height: 13px; flex: none; }
  .slogan {
    position: absolute;
    left: 30px; bottom: 24px;
    font-family: "Great Vibes", cursive;
    font-size: 26px;
    color: var(--mint);
  }
  .divider {
    position: absolute;
    left: 250px; top: 140px;
    width: 1px; height: 120px;
    background: var(--mint);
  }
  .services {
    position: absolute;
    left: 268px; top: 140px;
  }
  .services__title {
    font-family: "Great Vibes", cursive;
    font-size: 24px;
    color: var(--mint);
    margin-bottom: 6px;
    line-height: 1;
  }
  .services__item {
    font-size: 13px;
    color: var(--leaf);
    line-height: 1.45;
  }
</style>
</head>
<body>

  <section class="card card--front" aria-label="Decorative side">
    <div class="pattern pattern--top" role="img" aria-label="Pastel floral swirl pattern"></div>
    <div class="pattern pattern--bottom" role="img" aria-label="Pastel floral swirl pattern"></div>
    <div class="front-brand">
      <span class="brand-dot"></span>
      <span class="front-brand__name">Meadow Lane</span>
    </div>
  </section>

  <section class="card card--back" aria-label="Details side">
    <div class="wreath" role="img" aria-label="Floral wreath ornament"></div>
    <div class="back-title">Meadow Lane</div>

    <div class="contact">
      <div class="contact__name">Your Name Here</div>
      <div class="contact__role">Florist</div>
      <div class="contact__line">
        <svg viewBox="0 0 16 16"><circle cx="8" cy="8" r="8" fill="var(--mint)"/><rect x="5.5" y="3.5" width="5" height="9" rx="1" fill="none" stroke="#fff" stroke-width="1.2"/></svg>
        <span>123456789010</span>
      </div>
      <div class="contact__line">
        <svg viewBox="0 0 16 16"><circle cx="8" cy="8" r="8" fill="var(--mint)"/><rect x="4" y="5" width="8" height="6" fill="none" stroke="#fff" stroke-width="1.1"/><path d="M4 5l4 3.5L12 5" fill="none" stroke="#fff" stroke-width="1.1"/></svg>
        <span>youremail@here.com</span>
      </div>
    </div>

    <div class="divider"></div>

    <div class="services">
      <div class="services__title">Services</div>
      <div class="services__item">Your service here</div>
      <div class="services__item">Your service here</div>
      <div class="services__item">Your service here</div>
    </div>

    <div class="slogan">Your Slogan here</div>
  </section>

</body>
</html>
```